Korvane Works Business cards

We require somebody to design business cards for our new business.

Target Market(s)

Mining, haulage and civil.

Industry/Entity Type

Auto electrician in mining industry

Contact Information for Business Card

ABN, business email address, mobile number.

Colors
00AB8E
00BBA5
67D7C9
C6EFE9
E9F9F6

Requirements
Must have
• Services I offer: Breakdowns, Field Service, A/C Systems, Machine rewires, mine site vehicle fit outs

```html
<!DOCTYPE html>
<html lang="en">
<head>
<meta charset="utf-8">
<title>Korvane Works Business Cards</title>
<link href="https://fonts.googleapis.com/css2?family=Montserrat:wght@600;700&family=Open+Sans:wght@400;600;700&display=swap" rel="stylesheet">
<style>
  :root {
    --bg: #2b2b2b;
    --card: #161616;
    --teal: #5fc7c1;
    --teal-light: #67d7c9;
    --text: #f2f2f2;
    --silver-a: #5a5a5a;
    --silver-b: #e6e6e6;
  }
  * { margin: 0; padding: 0; box-sizing: border-box; }
  html, body { width: 1200px; height: 694px; overflow: hidden; }
  body {
    background: var(--bg);
    font-family: "Open Sans", sans-serif;
    color: var(--text);
    position: relative;
  }
  .card {
    position: absolute;
    top: 187px;
    width: 540px;
    height: 320px;
    background: var(--card);
    border-radius: 18px;
    overflow: hidden;
  }
  .card--front { left: 40px; }
  .card--back { left: 620px; }

  .brand {
    display: flex;
    align-items: center;
    gap: 10px;
    font-family: "Open Sans", sans-serif;
    font-weight: 700;
    color: var(--teal);
    letter-spacing: 1px;
    text-transform: uppercase;
  }
  .brand__mark {
    width: 14px; height: 14px;
    background: var(--teal);
  }
  .card--front .brand {
    position: absolute;
    top: 78px; left: 0; right: 0;
    justify-content: center;
    font-size: 34px;
  }
  .front__rule {
    position: absolute;
    top: 160px; left: 170px;
    width: 200px; height: 1px;
    background: var(--teal);
  }
  .services {
    position: absolute;
    top: 182px; left: 0; right: 0;
    text-align: center;
    font-size: 15px;
    line-height: 28px;
  }
  .services__label { color: var(--teal); font-weight: 600; }
  .services .dot { color: var(--teal); margin: 0 6px; }

  .person {
    position: absolute;
    top: 52px; left: 34px;
    padding-left: 22px;
  }
  .person__bar {
    position: absolute;
    left: 0; top: 2px;
    width: 8px; height: 52px;
    background: var(--teal);
  }
  .person__name {
    font-family: "Montserrat", sans-serif;
    font-weight: 700;
    font-size: 24px;
    color: var(--teal);
    text-transform: uppercase;
    letter-spacing: -0.5px;
  }
  .person__role { font-size: 14px; margin-top: 2px; }

  .contact {
    position: absolute;
    top: 146px; left: 56px;
    font-size: 13px;
    line-height: 20px;
  }
  .contact__address { margin-bottom: 10px; }
  .contact__row { display: flex; align-items: center; gap: 8px; }
  .contact__row svg { width: 12px; height: 12px; fill: var(--teal); flex: none; }

  .card--back .brand {
    position: absolute;
    top: 70px; right: 36px;
    font-size: 22px;
  }
  .abn {
    position: absolute;
    right: 0; bottom: 34px;
    width: 220px; height: 56px;
    background: var(--teal);
    clip-path: polygon(12% 0, 100% 0, 100% 100%, 0 100%);
    color: #111;
    font-size: 14px;
    display: flex; align-items: center; justify-content: center;
    padding-left: 20px;
  }
  .silver-strip {
    position: absolute;
    left: 0; right: 0; bottom: 0;
    height: 34px;
    background: linear-gradient(90deg, var(--silver-a), var(--silver-b) 45%, #8a8a8a 60%, var(--silver-b) 80%, var(--silver-a));
    clip-path: polygon(0 40%, 100% 0, 100% 100%, 0 100%);
  }
</style>
</head>
<body>

<section class="card card--front">
  <div class="brand"><span class="brand__mark"></span>Korvane Works</div>
  <div class="front__rule"></div>
  <p class="services">
    <span class="services__label">Services:</span> Breakdowns<span class="dot">•</span>Field Service<br>
    <span class="dot">•</span>A/C Systems<span class="dot">•</span>Machine rewires<span class="dot">•</span>Mine site vehicle fit outs
  </p>
</section>

<section class="card card--back">
  <div class="person">
    <span class="person__bar"></span>
    <h1 class="person__name">Marlow Teague</h1>
    <p class="person__role">Founder &amp; CEO</p>
  </div>

  <div class="contact">
    <p class="contact__address">418 Quarry Ridge Rd, Unit 12<br>Ashford Vale, QLD 4820</p>
    <p class="contact__row">
      <svg viewBox="0 0 24 24"><path d="M6.6 10.8a15.1 15.1 0 0 0 6.6 6.6l2.2-2.2a1 1 0 0 1 1-.25 11.4 11.4 0 0 0 3.6.57 1 1 0 0 1 1 1V20a1 1 0 0 1-1 1A17 17 0 0 1 3 4a1 1 0 0 1 1-1h3.5a1 1 0 0 1 1 1c0 1.25.2 2.45.57 3.57a1 1 0 0 1-.25 1z"/></svg>
      0491 762 305
    </p>
    <p class="contact__row">
      <svg viewBox="0 0 24 24"><path d="M2 5h20v14H2z M2 5l10 8 10-8" stroke="#161616" stroke-width="1.5"/></svg>
      info@korvaneworks.com
    </p>
    <p class="contact__row">
      <svg viewBox="0 0 24 24"><circle cx="12" cy="12" r="10"/></svg>
      korvaneworks.com
    </p>
  </div>

  <div class="brand"><span class="brand__mark"></span>Korvane Works</div>
  <div class="abn">ABN No - 48 302 917 655</div>
  <div class="silver-strip"></div>
</section>

</body>
</html>
```